Specialist Medical practice after professional trifold flyer design for patient information brochure

I am the Director of the Hollowbrook Clinic, a specialist medial and surgical practice in Australia. I am after a professional design of a patient information trifold flyer that can be used for web distribution or for commercial printing for upcoming educational event. The design would need to allow change of images and text to be used as template for future topics but have a common brand look across them. Colours would follow the logo, but primarily blue colours for the hollowbrook theme. The inside text needs to be clearly contrasted to the background for easy reading, as often elderly patients. The design would make use of curves or circles, but open for hexagonal, triangle square vector components. I have included an outline for the initial brochure and included images to include. Other stock background images can be used if they increase the impact of the design over included. A winning design is also one that could be modified to a 4 page bi-fold brochure

Target Market(s)

This will be provided to patients in GP practices, podiatry clinics, radiological practices. Aimed at patients to read and be compelled to look to site or get consultation with me

Industry/Entity Type

Medical

Font styles to use
Serif
Sans Serif

Colors
33a6d7
0355a3
86cfc6
cedeed
0292cd
85cae6

Requirements
Must have
• The front cover needs to engage the patient to pick up and read- yes I have a painful ankle and want to find out more. the goal for the inside is to provide the options but be able to direct to website for more info - website currently undergoing upgrade. After professional modern look. Not bright contrasting colours like many advertising brochures. Needs to able to have images and text changed but following same look to create new topics
Nice to have
• The focus is a Tri-fold brochure. Nice to be able to modify to bifold. A winning design would even offer both, or submit separate bifold and trifold. I am open to different versions of similar look. (eg option of brochure with curved elements, triangular or square, or hexagonal.
Should not have
• To many contrasting colours. Text must be easily read on background, either white or coloured background texture with transparency

```html
<!DOCTYPE html>
<html lang="en">
<head>
<meta charset="utf-8">
<title>My Painful Ankle – Trifold Brochure</title>
<link rel="stylesheet" href="https://fonts.googleapis.com/css2?family=Open+Sans:ital,wght@0,300;0,400;0,600;1,300;1,400&display=swap">
<style>
:root{
  --blue:#1b95c6;
  --heading:#1a8cc0;
  --slate:#485e6c;
  --slate-dark:#3b4f5c;
  --ink:#555d63;
  --ink-dark:#3f4a52;
  --paper:#ffffff;
  --bg:#d9d9d9;
  --xray-a:#5b6670;
  --xray-b:#1f262c;
}
*{box-sizing:border-box;margin:0;padding:0}
html,body{width:977px;height:1200px;overflow:hidden}
body{background:var(--bg);font-family:"Open Sans",Arial,sans-serif;color:var(--ink);position:relative}
.sheet{position:absolute;width:760px;height:535px;display:grid;grid-template-columns:repeat(3,1fr);background:var(--paper);box-shadow:0 4px 14px rgba(0,0,0,.25);overflow:hidden}
.sheet--outside{left:40px;top:40px}
.sheet--inside{left:177px;top:625px}
.panel{position:relative;overflow:hidden}
.plus{color:var(--heading);font-weight:600;margin-right:4px}
h2{font-weight:400;color:var(--heading);font-size:10.5px;letter-spacing:.1px;margin-bottom:4px}
p{font-weight:300;font-size:8.4px;line-height:1.28;margin-bottom:7px}
.photo{background:linear-gradient(160deg,#8a7a5c,#c9a86a 55%,#7c8d6a)}
/* outside: bio */
.bio{padding:32px 22px 0 32px}
.bio ul{list-style:none}
.bio li{font-size:8.4px;font-weight:300;line-height:1.28;margin-bottom:6px;padding-left:12px;position:relative}
.bio li::before{content:"+";position:absolute;left:0;top:-1px;color:var(--heading);font-weight:700}
.portrait{position:absolute;left:140px;top:304px;width:114px;height:231px;background:linear-gradient(180deg,#f3f5f7 0%,#dfe4e8 40%,#1f2328 72%)}
.doctor-tag{position:absolute;left:33px;top:391px;z-index:2;width:105px}
.doctor-tag strong{display:block;font-size:9.5px;font-weight:600;color:var(--ink-dark)}
.doctor-tag em{display:block;font-size:7.6px;font-weight:300;line-height:1.3}
/* outside: contact */
.contact{background:var(--slate);color:#fff;text-align:center}
.building{position:absolute;left:65px;top:174px;width:128px;height:68px;border:2px solid #fff;background:linear-gradient(180deg,#a9c4df,#d6e2ec 60%,#4f6b3d)}
.venue{position:absolute;top:272px;left:0;right:0;font-size:9.2px;line-height:1.45;font-weight:300}
.venue b{font-weight:400;font-size:9.8px}
.clinic-name{position:absolute;top:413px;left:0;right:0;display:flex;align-items:center;justify-content:center;gap:7px;font-size:15px;font-weight:600;letter-spacing:.5px;text-transform:uppercase}
.clinic-name i{width:14px;height:14px;border-radius:50%;background:#fff;display:block}
.calls{position:absolute;top:465px;left:0;right:0;font-size:12.6px;line-height:1.55;font-weight:400}
.mail{position:absolute;top:506px;left:0;right:0;font-size:9px;font-weight:300}
/* outside: cover */
.cover{background:var(--blue)}
.cover .photo{position:absolute;left:0;top:0;right:0;height:330px}
.cover svg{position:absolute;left:0;top:0}
.badge{position:absolute;left:162px;top:255px;width:72px;height:72px;border-radius:50%;background:var(--slate-dark);color:#fff;font-size:10.5px;line-height:1.05;font-weight:400;display:flex;align-items:center;justify-content:center;text-align:center;transform:rotate(22deg)}
.title{position:absolute;left:50px;top:301px;font-size:40px;line-height:37px;font-weight:400;color:#fff}
.title span{color:var(--slate-dark);display:block}
.byline{position:absolute;left:47px;top:413px;color:#fff;font-size:9.2px;line-height:1.3}
.byline em{font-size:7.8px;font-weight:300;display:block}
.web-tab{position:absolute;left:47px;top:503px;width:157px;height:32px;background:var(--slate);color:#fff;font-size:8.6px;display:flex;align-items:center;justify-content:center;font-weight:300}
/* inside */
.decision{color:#fff}
.decision .content{position:absolute;left:42px;top:40px;right:12px;z-index:1}
.decision h2{color:#fff}
.decision svg{position:absolute;left:0;top:0}
.desk-photo{position:absolute;left:148px;top:215px;width:98px;height:98px;border-radius:50%;border:3px solid var(--blue);background:linear-gradient(135deg,#eef2f5,#9bb4c6 60%,#5f7c90)}
.foot-art{position:absolute;left:0;top:320px;width:253px;height:215px;background:radial-gradient(ellipse at 45% 65%,rgba(120,175,205,.55),rgba(40,60,75,0) 65%)}
.quote{position:absolute;left:157px;top:334px;font-style:italic;font-weight:300;font-size:10.2px;line-height:1.3;color:#fff}
.col{padding:34px 14px 0 22px}
.col p{color:var(--ink)}
.xray{float:right;width:100px;height:100px;border-radius:50%;border:4px solid var(--blue);background:radial-gradient(circle at 45% 45%,var(--xray-a),var(--xray-b) 75%);margin:2px -2px 6px 10px}
.link{font-weight:600;color:var(--heading);font-size:8.4px}
.section-gap{margin-top:10px;clear:both}
</style>
</head>
<body>

<section class="sheet sheet--outside">
  <div class="panel bio">
    <h2><span class="plus">+</span>DR MARTIN HALE</h2>
    <p>Dr Martin Hale is an Australian trained Orthopaedic Surgeon who has a primary focus in the treatment of conditions of the foot and ankle. He has completed post fellowship training in Foot and Ankle surgery both locally and internationally, and continues to update himself in the latest techniques.</p>
    <p>Conditions treated Dr Hale provides assessment and treatment of all foot and ankle conditions. He has special interest in the following:</p>
    <ul>
      <li>Minimally invasive treatment for bunions and toe deformities.</li>
      <li>Joint sparing procedures for arthritis or deformity, including the Sorbix implant.</li>
      <li>Joint fusion procedures for arthritis of the feet and ankle.</li>
      <li>Sports injuries and tendinopathies.</li>
      <li>Total ankle replacement and deformity correction of the foot and ankle.</li>
    </ul>
    <div class="portrait" role="img" aria-label="Portrait of the surgeon in a dark suit and blue tie"></div>
    <div class="doctor-tag"><strong>Dr Martin Hale</strong><em>MBBS (Hons), FRACS (Ortho),<br>FA (Ortho)</em></div>
  </div>

  <div class="panel contact">
    <div class="building" role="img" aria-label="Photo of the private hospital building"></div>
    <div class="venue">
      <b>KESTREL BAY PRIVATE HOSPITAL</b><br>Suite 12, Level 4<br>88 Harbour Street<br>Kestrel Bay NSW<br><br>
      <b>HOLLOWBROOK CLINIC</b><br>14 River Lane<br>Tallow Creek NSW
    </div>
    <div class="clinic-name"><i></i>Hollowbrook Clinic</div>
    <div class="calls">CALL US: (02) 5550 1234<br>FAX: (02) 5550 1299</div>
    <div class="mail">info@hollowbrookclinic.com.au</div>
  </div>

  <div class="panel cover">
    <div class="photo" role="img" aria-label="Photo of a runner holding a painful ankle on a sunny field"></div>
    <svg width="254" height="535" viewBox="0 0 254 535" aria-hidden="true">
      <path d="M0,245 Q120,255 254,312 L254,535 L0,535 Z" fill="#1b95c6"/>
    </svg>
    <div class="badge">Solutions<br>for ankle<br>arthritis</div>
    <div class="title">MY<span>PAINFUL</span>ANKLE</div>
    <div class="byline">Dr Martin Hale<em>Orthopaedic Foot and Ankle Surgeon</em></div>
    <div class="web-tab">www.hollowbrookclinic.com.au</div>
  </div>
</section>

<section class="sheet sheet--inside">
  <div class="panel decision">
    <svg width="254" height="535" viewBox="0 0 254 535" aria-hidden="true">
      <defs>
        <linearGradient id="deep" x1="0" y1="0" x2="0" y2="1">
          <stop offset="0" stop-color="#5a7282"/>
          <stop offset="1" stop-color="#2e3d47"/>
        </linearGradient>
      </defs>
      <rect width="254" height="535" fill="#1b95c6"/>
      <path d="M0,300 Q130,275 254,225 L254,535 L0,535 Z" fill="url(#deep)"/>
    </svg>
    <div class="foot-art" role="img" aria-label="Illustration of a foot skeleton with a highlighted ankle joint"></div>
    <div class="content">
      <h2><span class="plus" style="color:#fff">+</span>MAKE A INFORMED DECISION</h2>
      <p>When pain medication, activity modification and shoe ware modification is no longer effective to control the pain then then it is worthwhile discussing with your GP for referral to Dr Martin Hale for an opinion on further treatment. As an Orthopaedic Foot and Ankle surgeon, he will be able to assess your conditions and give advice on the best options for your treatment.</p>
      <p>The decision on the best option is based on your age, activity level, existing medical problems, previous ankle treatment and your expected outcome from treatment. In the situation of end stage arthritis options consist of either Ankle fusion or Total Ankle replacement.</p>
    </div>
    <div class="desk-photo" role="img" aria-label="Photo of a stethoscope on a keyboard"></div>
    <div class="quote">“Dr Martin Hale<br>can give you advice<br>on the best options<br>for your treatment.”</div>
  </div>

  <div class="panel col">
    <h2><span class="plus">+</span>ANKLE ARTHRITIS</h2>
    <p>Ankle arthritis is a painful condition where there is loss of cartilage from the ankle joint surface.</p>
    <div class="xray" role="img" aria-label="X-ray of an arthritic ankle joint"></div>
    <p>Although not as common as knee or hip arthritis, pain can be debilitating affecting quality of life.</p>
    <p>Arthritis of the joint can be caused by trauma joint such as fracture or recurrent instability or secondary from inflammatory conditions such as rheumatoid arthritis.</p>
    <p>Pain from the joint will occur with activity causing a limp, limiting walking speed and distance. Often there is swelling of the joint with progressive loss of motion.</p>
    <p>Diagnosis is made with examination of the ankle and weight bearing x-rays showing loss of joint space.</p>
    <h2 class="section-gap"><span class="plus">+</span>ANKLE FUSION SURGERY</h2>
    <p>This operation aims to stiffen the ankle joint by fusing the tibia and talus together in the optimal position for function.</p>
    <div class="xray" role="img" aria-label="X-ray of an ankle fusion with screws and plate"></div>
    <p>The common thought is that there will be no movement of the foot, and the patient will walk with a limp. The fusion only occurs at the ankle joint, leaving motion available to the surrounding joints. Although there is decreased motion, you will walk more normally after a fusion without a limp as the pain to the joint is removed.</p>
    <p style="clear:both">For more information on ankle fusion, risks and recovery visit our website:<br><span class="link">www.hollowbrookclinic.com.au/Ankle-Fusion</span></p>
  </div>

  <div class="panel col">
    <h2><span class="plus">+</span>TOTAL ANKLE REPLACEMENT SURGERY</h2>
    <p>In suitable patients there may be the option to maintain joint motion and perform a Total Ankle Replacement.</p>
    <div class="xray" role="img" aria-label="X-ray of a total ankle replacement implant"></div>
    <p>Like a hip or knee replacement operation, the arthritic joint is removed and replaced with an artificial joint. Like an ankle fusion there will alleviation of the pain and limp with maintenance of the ankle joint motion. Recovery to walking post-surgery is often much sooner than with ankle fusion. Dr Martin Hale if one of the few surgeons to have completed an international fellowship in ankle replacement surgery and has been performing the technique since 2008. He is currently performing the technique using the Meridian Total ankle with TruAlign guides.</p>
    <p style="clear:both">For more information on ankle fusion, risks and recovery visit our website:<br><span class="link">www.hollowbrookclinic.com.au/Ankle-Replacement</span></p>
    <h2 class="section-gap"><span class="plus">+</span>RESULTS OF SURGERY</h2>
    <p>Successful surgery in the suitable patient will help resolve the pain associated with the ankle arthritis. Ankle Fusion surgery is ideal for patients with heavy labour work, allowing them to return to previous activities. There may be the risk of arthritis to surrounding joints in the future, but often this occurs many years down the track. Results from Total Ankle replacement surgery have been improving over the years, but there is known risks of loosening, cyst formation or failure of the joint over time that can occur in some patients. It is important to have a opinion from an Orthopaedic Foot and Ankle Surgeon experienced in the these procedure to determine which procedure will provide the best long term solution for you.</p>
  </div>
</section>

</body>
</html>
```